Brivora Collective Business Card Design

We need a business card design for Brivora Collective. We are a healthcare recruiting, wellness and education company. We partner with medical facilities to find quality candidates. We also offer free wellness courses.
The final design should communicate an emphasis on recruiting and wellness
The main purpose of the business card is to utilized it for networking events, give to hospitals, executives, VCs surgery centers and clinics. I want it to be sleek, clean, use of our brand colors and professional.

```html
<!DOCTYPE html>
<html lang="en">
<head>
<meta charset="utf-8">
<title>Brivora Collective Business Card</title>
<link href="https://fonts.googleapis.com/css2?family=Arimo:wght@400;500;700&display=swap" rel="stylesheet">
<style>
  :root {
    --backdrop: #3a3b3d;
    --card: #ffffff;
    --brand-dark: #0b5c4f;
    --brand-soft: #6fa89d;
    --text-grey: #5b5e61;
  }
  html, body {
    margin: 0;
    width: 1200px;
    height: 900px;
    overflow: hidden;
    background: var(--backdrop);
    font-family: "Arimo", Arial, sans-serif;
  }
  .stage {
    position: relative;
    width: 1200px;
    height: 900px;
  }
  .card {
    position: absolute;
    left: 240px;
    width: 720px;
    height: 410px;
    background: linear-gradient(120deg, #ffffff 0%, #f1f1f1 100%);
    overflow: hidden;
    box-shadow: 0 10px 24px rgba(0,0,0,0.35);
  }
  .card--front { top: 28px; }
  .card--back { top: 462px; }
  .card__shapes {
    position: absolute;
    inset: 0;
    width: 720px;
    height: 410px;
  }
  .brand-name {
    position: absolute;
    display: flex;
    align-items: center;
    gap: 14px;
    color: var(--brand-dark);
    font-weight: 500;
    letter-spacing: -0.5px;
    margin: 0;
    white-space: nowrap;
  }
  .brand-name__mark {
    width: 22px;
    height: 22px;
    background: var(--brand-dark);
    flex: none;
  }
  .card--front .brand-name {
    left: 48px;
    top: 70px;
    font-size: 54px;
    line-height: 1;
  }
  .mission {
    position: absolute;
    right: 48px;
    top: 180px;
    width: 300px;
    text-align: right;
  }
  .mission__title {
    margin: 0 0 8px;
    color: var(--brand-dark);
    font-weight: 700;
    font-size: 19px;
  }
  .mission__text {
    margin: 0;
    color: var(--text-grey);
    font-size: 15.5px;
    line-height: 1.32;
  }
  .card--back .brand-name {
    right: 46px;
    top: 96px;
    font-size: 38px;
    line-height: 1;
  }
  .person {
    position: absolute;
    left: 52px;
    top: 118px;
  }
  .person__name {
    margin: 0;
    color: var(--brand-dark);
    font-weight: 700;
    font-size: 21px;
    letter-spacing: 0.3px;
  }
  .person__role {
    margin: 4px 0 0;
    color: var(--text-grey);
    font-size: 17px;
  }
  .contact {
    position: absolute;
    left: 52px;
    top: 205px;
    margin: 0;
    padding: 0;
    list-style: none;
  }
  .contact__item {
    display: flex;
    align-items: center;
    gap: 12px;
    color: var(--text-grey);
    font-size: 17px;
    height: 28px;
  }
  .contact__icon {
    width: 17px;
    height: 17px;
    fill: var(--brand-dark);
    flex: none;
  }
  .website {
    position: absolute;
    right: 24px;
    top: 342px;
    margin: 0;
    color: var(--brand-dark);
    font-size: 16px;
    white-space: nowrap;
  }
</style>
</head>
<body>
<main class="stage">

  <section class="card card--front" aria-label="Card front">
    <svg class="card__shapes" viewBox="0 0 720 410" aria-hidden="true">
      <path d="M0 320 H262 Q292 320 304 338 L346 410 H0 Z" fill="var(--brand-soft)"/>
      <polygon points="350,368 720,300 720,340 372,410 362,410" fill="var(--brand-dark)"/>
    </svg>
    <h1 class="brand-name"><span class="brand-name__mark"></span>Brivora Collective</h1>
    <div class="mission">
      <h2 class="mission__title">Our Mission</h2>
      <p class="mission__text">We provide wellness and career support to healthcare professionals, connection with local medical centers, and sustainable employment solutions.</p>
    </div>
  </section>

  <section class="card card--back" aria-label="Card back">
    <svg class="card__shapes" viewBox="0 0 720 410" aria-hidden="true">
      <path d="M498 410 V312 Q498 286 524 286 H720 V410 Z" fill="var(--brand-soft)"/>
      <polygon points="0,378 482,348 482,410 0,410" fill="var(--brand-dark)"/>
    </svg>
    <p class="brand-name"><span class="brand-name__mark"></span>Brivora Collective</p>
    <div class="person">
      <h2 class="person__name">MARTA ELLISON</h2>
      <p class="person__role">Co-Founder, CEO</p>
    </div>
    <ul class="contact">
      <li class="contact__item">
        <svg class="contact__icon" viewBox="0 0 24 24" aria-hidden="true"><path d="M6.6 10.8a15.1 15.1 0 0 0 6.6 6.6l2.2-2.2a1 1 0 0 1 1-.25 11.4 11.4 0 0 0 3.6.57 1 1 0 0 1 1 1V20a1 1 0 0 1-1 1A17 17 0 0 1 3 4a1 1 0 0 1 1-1h3.5a1 1 0 0 1 1 1c0 1.250.2 2.450.57 3.57a1 1 0 0 1-.25 1z"/></svg>
        000-000-0000
      </li>
      <li class="contact__item">
        <svg class="contact__icon" viewBox="0 0 24 24" aria-hidden="true"><path d="M2 5h20v14H2z M4 7v.5l8 5 8-5V7l-8 5z" fill-rule="evenodd"/></svg>
        info@brivoracollective.com
      </li>
      <li class="contact__item">
        <svg class="contact__icon" viewBox="0 0 24 24" aria-hidden="true"><path d="M12 2a7 7 0 0 0-7 7c0 5 7 13 7 13s7-8 7-13a7 7 0 0 0-7-7zm0 9.5A2.5 2.5 0 1 1 12 6.5a2.5 2.5 0 0 1 0 5z"/></svg>
        Austin, Texas 78701, US
      </li>
    </ul>
    <p class="website">brivoracollective.com</p>
  </section>

</main>
</body>
</html>
```